依頼概要
■依頼の目的/概要
母の日用新品種アジサイの販促ポスターの作成依頼です。

■依頼詳細
・ポスターサイズはA2を予定しています。
・ターゲット
大人可愛い、北欧系のインテリアやおしゃれなライフスタイルを好む30代女性
・テーマ、カラー
ナチュラル系、淡めの暖色系、おしゃれなカフェや雑貨屋さんに合うような雰囲気
※実際にはポスターを貼って頂くところは花屋さんですが、花を買ったことがない人にも興味を持って頂くのが狙いです。

補足情報は添付ファイルをご確認ください。

細かい所はやり取りしながら相談させて頂きたいと思います。
よろしくお願いいたします。
■ 選んだ理由

素敵で可愛らしいデザインがいくつもあり迷いましたが、
私達の目指すコンセプトやターゲットに当てはまるデザイン案を
選ばせていただきました。

■ 提案者全員のお礼・コメント

ご提案くださったランサーの皆さまへ

予想以上にたくさんのご提案をいただき、大変有難く思っております。
このアジサイは私達にとって、とても大切な品種で思い入れがあります。

最終決定するまで、随分迷いました。
素敵なデザインをご提案くださった皆さまにこの場を借りて感謝申し上げます。
有難うございました。

また機会がありましたら、その際はよろしくお願い致します。

```html
<!DOCTYPE html>
<html lang="ja">
<head>
<meta charset="utf-8">
<title>桃霞 Mother's Day</title>
<link rel="stylesheet" href="https://fonts.googleapis.com/css2?family=Great+Vibes&family=Kosugi+Maru&family=Playfair+Display:wght@400;700&family=Quicksand:wght@500&display=swap">
<style>
  :root {
    --wood: #ece7e1;
    --wood-light: #f7f4f0;
    --orange: #f6b46a;
    --peach: #f9cf9c;
    --blush: #f5c9c4;
    --green: #86b83a;
    --pink: #c96a9b;
    --pink-soft: #d98db3;
    --leaf: #5c8a3a;
    --bloom: #e58fb0;
    --white: #ffffff;
  }
  html, body { margin: 0; padding: 0; overflow: hidden; }
  body { width: 846px; height: 1200px; }
  .poster {
    position: relative;
    width: 846px;
    height: 1200px;
    overflow: hidden;
    background: linear-gradient(180deg, var(--wood-light) 0%, var(--wood) 100%);
    font-family: "Quicksand", sans-serif;
  }
  .backdrop { position: absolute; inset: 0; }
  .product-name {
    position: absolute;
    top: 150px; left: 0;
    width: 846px;
    margin: 0;
    text-align: center;
    white-space: nowrap;
    font-family: "Kosugi Maru", sans-serif;
    font-weight: 400;
    font-size: 104px;
    letter-spacing: 36px;
    text-indent: 36px;
    color: var(--green);
    line-height: 1;
  }
  .product-reading {
    position: absolute;
    top: 268px; left: 0;
    width: 846px;
    text-align: center;
    white-space: nowrap;
    font-size: 28px;
    color: var(--green);
    letter-spacing: 1px;
    line-height: 1;
  }
  .headline {
    position: absolute;
    top: 310px; left: 0;
    width: 846px;
    text-align: center;
    margin: 0;
    color: var(--pink);
    font-weight: 400;
  }
  .headline-script {
    display: block;
    font-family: "Great Vibes", cursive;
    font-size: 180px;
    line-height: 200px;
    white-space: nowrap;
  }
  .headline-day {
    display: block;
    font-family: "Playfair Display", serif;
    font-size: 96px;
    letter-spacing: 6px;
    line-height: 110px;
  }
  .laurel {
    position: absolute;
    top: 652px; left: 268px;
    width: 310px; height: 34px;
    border-radius: 17px;
    opacity: 0.45;
    background: linear-gradient(90deg, transparent, var(--pink-soft) 20%, var(--pink-soft) 80%, transparent);
  }
  .thanks {
    position: absolute;
    top: 712px; left: 0;
    width: 846px;
    text-align: center;
    font-family: "Playfair Display", serif;
    font-size: 34px;
    letter-spacing: 8px;
    color: var(--pink-soft);
    line-height: 1;
  }
  .bouquet {
    position: absolute;
    left: -30px; top: 800px;
    width: 906px; height: 440px;
    border-radius: 50% 50% 0 0 / 40% 40% 0 0;
    background: radial-gradient(ellipse at 50% 30%, var(--bloom) 0%, #d67aa0 35%, var(--leaf) 75%, #3f6a2a 100%);
  }
  .maker {
    position: absolute;
    left: 0; bottom: 60px;
    width: 846px;
    display: flex;
    justify-content: center;
    align-items: center;
    gap: 12px;
    font-family: "Kosugi Maru", sans-serif;
    font-size: 22px;
    color: var(--white);
  }
  .maker-dot {
    width: 16px; height: 16px;
    border-radius: 50%;
    background: var(--white);
  }
</style>
</head>
<body>
<main class="poster">
  <svg class="backdrop" width="846" height="1200" viewBox="0 0 846 1200" aria-hidden="true">
    <circle cx="70" cy="40" r="120" fill="var(--orange)" opacity="0.55"/>
    <circle cx="180" cy="-10" r="70" fill="var(--peach)" opacity="0.6"/>
    <circle cx="700" cy="60" r="180" fill="var(--orange)" opacity="0.5"/>
    <circle cx="810" cy="420" r="140" fill="var(--peach)" opacity="0.55"/>
    <circle cx="30" cy="580" r="150" fill="var(--blush)" opacity="0.5"/>
    <circle cx="800" cy="760" r="110" fill="var(--orange)" opacity="0.4"/>
    <circle cx="120" cy="300" r="60" fill="var(--peach)" opacity="0.35"/>
  </svg>

  <h1 class="product-name">桃霞</h1>
  <div class="product-reading">momo kasumi</div>

  <h2 class="headline">
    <span class="headline-script">Mother's</span>
    <span class="headline-day">DAY</span>
  </h2>

  <div class="laurel" role="img" aria-label="Small pink laurel branch ornament"></div>

  <div class="thanks">THANK YOU</div>

  <div class="bouquet" role="img" aria-label="Photograph of a potted pink hydrangea with green leaves"></div>

  <div class="maker">
    <span class="maker-dot"></span>
    <span>陽だまり花卉研究会</span>
  </div>
</main>
</body>
</html>
```